"Het Zaakkompas" needs a new Web Design

We need a web design for to support the startup of a new Activity.

Het Zaakkompas is a company that offers consulting services towards SMB based in Belgium. Focus of the consultancy is:
-Marketing
-Sales
-ICT

We would like to see designs that use the color blue and that fit's with our logo.

The website should communicate trust and expertise.

Main goal of the website is to attract new professional customers

We think of providing following content on the site:
-Home Page
-Who we are (present our 3 team members)
-How we work
-Skills we offer
-Contact us
-Groeiateliers (Free workshops we offer on a regular base)
-Blog

In a later stage:
-Testimonials
-Create & Integrate an animation where we present our services

Call To Actions:
-Register for our newsletter
-Register for a Groeiatelier
-Ask a free intake meeting

CTA's will change from time to time.
Design has to be responsive

Site will be made in wordpress. Design should fit in a existing template so we do not have to start from scratch.

see www.zaakkompas.be

The logo attached is just new. Feel free if yoy have any suggestions to approve this!

Target Market(s)

SMB companies that likes to grow and and expand there business

Industry/Entity Type

Management Consulting

Contact Information for Business Card

I was thinking of including there a picture in from ourselves

Coding

Coded - Design and coding required

Number of Pages Required

5+ page

Font styles to use
Sans Serif

Colors
3277b5
0592cd
33a6d7
85cae6
85acd2
fcfafc

Requirements
Must have
• I'm using the themes from Velvet Layouts
• For example Orla. Should nice tu use this.
• http://www.velvetlayouts.com/gallery/orla/
• I like the design from this site.
• http://www.ondernemershulp-veldhoek.be/#home
• Header menu can better but the thing I realy like is the design of the "Missie" page. the "animation"
Should not have
• I do not want a traditional design.
• Other sites I like:
• https://www.mailpeloton.com/
• https://www.staylantern.com
• https://www.tallygrove.com
• http://www.voxtrellis.com
• http://www.craftbazaru.com/

```html
<!DOCTYPE html>
<html lang="en">
<head>
<meta charset="utf-8">
<title>Het Zaakkompas – Consulting services towards SMB</title>
<link href="https://fonts.googleapis.com/css2?family=Open+Sans:wght@300;400;600;700&display=swap" rel="stylesheet">
<style>
:root{
  --blue:#3277b5;
  --blue-deep:#1d5a92;
  --nav:#1f5f98;
  --nav-active:#174b7a;
  --sky:#33a6d7;
  --pale:#85cae6;
  --ink:#333a42;
  --muted:#7b838b;
  --line:#e3e6ea;
  --bg:#ffffff;
  --soft:#f4f6f8;
  --footer:#1d2631;
  --footer-bar:#151c25;
  --cta:#2f78bd;
}
*{box-sizing:border-box;margin:0;padding:0}
html,body{width:1200px;height:2224px;overflow:hidden}
body{font-family:"Open Sans",Arial,sans-serif;color:var(--ink);background:var(--bg);font-size:13px;line-height:1.6}
.wrap{width:1080px;margin:0 auto;position:relative}

/* header */
.topbar{height:120px}
.topbar .wrap{display:flex;align-items:center;justify-content:space-between;height:120px}
.brand{display:flex;align-items:center;gap:12px}
.brand-mark{width:34px;height:34px;background:var(--blue)}
.brand-name{font-size:26px;font-weight:600;color:var(--blue-deep);letter-spacing:.3px}
.contact-mini{display:flex;align-items:center;gap:10px}
.phone{display:flex;align-items:center;gap:6px;font-weight:600;font-size:15px;color:var(--ink);margin-right:8px}
.social-dot{width:28px;height:28px;border:1px solid #c9cfd6;border-radius:50%}

.mainnav{height:42px;background:var(--nav)}
.mainnav ul{list-style:none;display:flex;height:42px}
.mainnav li{color:#fff;font-size:12px;font-weight:600;letter-spacing:.5px;padding:0 27px;line-height:42px}
.mainnav li.active{background:var(--nav-active)}

/* hero */
.hero{height:538px;position:relative;background:linear-gradient(100deg,#d9dde2 0%,#b7bcc4 35%,#e7e2dd 60%,#c9ccd2 100%)}
.hero-caption{position:absolute;left:110px;top:345px;color:#fff;text-shadow:0 1px 4px rgba(0,0,0,.35)}
.hero-caption h1{font-size:46px;font-weight:400;line-height:1.15;letter-spacing:.5px}
.hero-caption p{font-size:32px;font-weight:300;letter-spacing:.5px}

/* services */
.services{padding:115px 0 60px}
.services .wrap{display:flex;justify-content:space-between;padding:0 40px}
.service{display:flex;gap:22px;width:300px}
.service-icon{flex:none;width:74px;height:74px;border-radius:50%;background:var(--nav);display:flex;align-items:center;justify-content:center}
.service h3{font-size:14px;font-weight:700;color:var(--blue);margin:8px 0 4px}
.service p{font-size:11px;color:var(--muted);line-height:1.5}

/* who we are */
.who{border-top:1px solid var(--line);padding:28px 0 40px;text-align:center}
.section-title{font-size:22px;font-weight:600;color:var(--blue-deep);letter-spacing:.5px}
.who p{font-size:11.5px;color:var(--muted);margin:14px auto 0;width:1040px;text-align:left;line-height:1.7}

/* our services */
.split .wrap{display:flex;gap:40px;padding-top:30px}
.video{width:500px;height:300px;border:1px solid var(--line);padding:6px;background:#fff}
.video-frame{width:100%;height:100%;position:relative;background:linear-gradient(120deg,#5a6470,#b9c0c9 45%,#e3e0db 70%,#7c8591)}
.play{position:absolute;left:50%;top:50%;transform:translate(-50%,-50%)}
.video-bar{position:absolute;left:0;right:0;bottom:0;height:26px;background:rgba(0,0,0,.65)}
.split-text{flex:1;padding-top:4px}
.split-text h2{font-size:19px;font-weight:600;color:var(--blue-deep);margin-bottom:10px}
.split-text p{font-size:11.5px;color:var(--muted);margin-bottom:14px;line-height:1.7}
.btn{display:inline-block;background:var(--blue);color:#fff;font-size:12px;font-weight:600;padding:8px 22px;border-radius:3px}

/* blog */
.blog{padding-top:72px}
.blog-head{display:flex;justify-content:space-between;align-items:center;border-bottom:1px solid var(--line);padding-bottom:8px}
.blog-head h2{font-size:16px;font-weight:700;color:var(--ink)}
.arrows{display:flex;gap:6px}
.blog-list{display:flex;gap:60px;padding-top:22px}
.post{display:flex;gap:16px;width:510px}
.post-thumb{flex:none;width:210px;height:130px;background:linear-gradient(135deg,#c6ccd3,#eceae6 50%,#9aa6b3)}
.post h4{font-size:11px;font-weight:700;color:var(--ink);margin-top:8px}
.post .date{font-size:10px;color:var(--sky)}
.post p{font-size:10.5px;color:var(--muted);line-height:1.55;margin:6px 0}
.post .more{font-size:10.5px;color:var(--blue);font-weight:600}

/* cta band */
.cta{margin-top:75px;height:140px;background:var(--cta)}
.cta .wrap{display:flex;justify-content:space-between;align-items:center;height:140px;padding:0 40px}
.cta-btn{width:290px;height:44px;background:#fff;color:var(--blue-deep);font-size:12px;font-weight:700;letter-spacing:.4px;display:flex;align-items:center;justify-content:center;border-radius:3px}

/* footer */
.footer{background:var(--footer);height:220px;color:#aeb6bf}
.footer .wrap{display:flex;gap:40px;padding-top:28px}
.fcol h5{color:#fff;font-size:13px;font-weight:700;margin-bottom:10px;letter-spacing:.3px}
.fcol{font-size:11px;line-height:1.9}
.links{width:180px}
.links li{list-style:none}
.testi{width:290px}
.touch{width:260px}
.follow{flex:1}
.follow-dots{display:flex;gap:10px;margin-top:10px}
.follow-dots span{width:32px;height:32px;border-radius:50%;background:var(--blue)}
.copyright{background:var(--footer-bar);height:44px;color:#8b949e;font-size:11px;text-align:center;line-height:44px}
</style>
</head>
<body>

<header class="topbar">
  <div class="wrap">
    <div class="brand"><span class="brand-mark"></span><span class="brand-name">Het Zaakkompas</span></div>
    <div class="contact-mini">
      <span class="phone">
        <svg width="16" height="16" viewBox="0 0 24 24"><path fill="#3277b5" d="M6.6 10.8a15 15 0 0 0 6.6 6.6l2.2-2.2c.3-.3.7-.4 1-.2 1.1.4 2.3.6 3.6.6.6 0 1 .4 1 1V20c0 .6-.4 1-1 1C10.6 21 3 13.4 3 4c0-.6.4-1 1-1h3.5c.6 0 1 .4 1 1 0 1.2.2 2.4.6 3.6.1.3 0 .7-.2 1z"/></svg>
        248-555-0147
      </span>
      <span class="social-dot"></span>
      <span class="social-dot"></span>
      <span class="social-dot"></span>
    </div>
  </div>
</header>

<nav class="mainnav">
  <div class="wrap">
    <ul>
      <li class="active">HOME</li><li>WHO WE ARE</li><li>HOW WE WORK</li><li>SKILLS</li><li>GROEIATELIER</li><li>BLOG</li><li>CONTACT</li>
    </ul>
  </div>
</nav>

<section class="hero" role="img" aria-label="Photo of a smiling consultant at her desk in a bright office, with colleagues in the background">
  <div class="hero-caption">
    <h1>CONSULTING SERVICES</h1>
    <p>TOWARDS SMB</p>
  </div>
</section>

<section class="services">
  <div class="wrap">
    <div class="service">
      <div class="service-icon"><svg width="30" height="30" viewBox="0 0 24 24"><circle cx="12" cy="8" r="4" fill="#fff"/><path d="M4 21c0-4.4 3.6-7 8-7s8 2.6 8 7z" fill="#fff"/></svg></div>
      <div><h3>MARKETING</h3><p>Plans that bring the right clients to your door, step by step.</p></div>
    </div>
    <div class="service">
      <div class="service-icon"><svg width="30" height="30" viewBox="0 0 24 24"><path d="M2 11 22 3l-6 18-4-7z" fill="#fff"/><path d="M12 14 22 3" stroke="#1f5f98" stroke-width="1.5"/></svg></div>
      <div><h3>SALES</h3><p>Clear sales routines that turn first contacts into loyal customers.</p></div>
    </div>
    <div class="service">
      <div class="service-icon"><svg width="30" height="30" viewBox="0 0 24 24"><g fill="#fff"><circle cx="12" cy="12" r="6.5"/><rect x="10.5" y="1.5" width="3" height="5"/><rect x="10.5" y="17.5" width="3" height="5"/><rect x="1.5" y="10.5" width="5" height="3"/><rect x="17.5" y="10.5" width="5" height="3"/></g><circle cx="12" cy="12" r="2.6" fill="#1f5f98"/></svg></div>
      <div><h3>ICT</h3><p>Smart, simple tools that keep your business running and connected.</p></div>
    </div>
  </div>
</section>

<section class="who">
  <div class="wrap">
    <h2 class="section-title">WHO WE ARE</h2>
    <p>We are three experienced consultants who help small and medium businesses grow. We listen first, then build practical plans for marketing, sales and ICT that fit your budget, your team and your ambitions. Every project starts with a free intake meeting, so we understand where you stand and where you want to go.</p>
  </div>
</section>

<section class="split">
  <div class="wrap">
    <div class="video">
      <div class="video-frame" role="img" aria-label="Video still of two consultants in a meeting with a client">
        <svg class="play" width="56" height="56" viewBox="0 0 56 56"><circle cx="28" cy="28" r="27" fill="rgba(0,0,0,.45)"/><path d="M22 17 40 28 22 39z" fill="#fff"/></svg>
        <div class="video-bar"></div>
      </div>
    </div>
    <div class="split-text">
      <h2>OUR SERVICES</h2>
      <p>Our approach is hands-on: we work next to you and your team, not above you. From the first analysis to the final rollout, we keep things clear and measurable.</p>
      <p>We combine marketing, sales and ICT know-how in one partner, so your growth plan stays coherent and every step supports the next.</p>
      <span class="btn">Read More</span>
    </div>
  </div>
</section>

<section class="blog">
  <div class="wrap">
    <div class="blog-head">
      <h2>LATEST BLOG</h2>
      <div class="arrows">
        <svg width="12" height="12" viewBox="0 0 12 12"><path d="M8 2 4 6l4 4" stroke="#9aa3ad" stroke-width="2" fill="none"/></svg>
        <svg width="12" height="12" viewBox="0 0 12 12"><path d="M4 2l4 4-4 4" stroke="#9aa3ad" stroke-width="2" fill="none"/></svg>
      </div>
    </div>
    <div class="blog-list">
      <article class="post">
        <div class="post-thumb" role="img" aria-label="Photo of a team gathered around a laptop"></div>
        <div><h4>SIMPLE SUMMARY TEXT</h4><div class="date">12 Apr 2015</div><p>Five quick checks to see if your website really brings in new leads this year.</p><span class="more">Read More »</span></div>
      </article>
      <article class="post">
        <div class="post-thumb" role="img" aria-label="Photo of a business handshake across a table"></div>
        <div><h4>SIMPLE SUMMARY TEXT</h4><div class="date">19 Apr 2015</div><p>How a short weekly sales meeting keeps your whole team focused on the right goals.</p><span class="more">Read More »</span></div>
      </article>
    </div>
  </div>
</section>

<section class="cta">
  <div class="wrap">
    <span class="cta-btn">REGISTER FOR OUR NEWSLETTER</span>
    <span class="cta-btn">REGISTER FOR A GROEIATELIER</span>
    <span class="cta-btn">ASK A FREE INTAKE MEETING</span>
  </div>
</section>

<footer class="footer">
  <div class="wrap">
    <div class="fcol links"><h5>LINKS</h5><ul><li>Who we are</li><li>How we work</li><li>Skills</li><li>Groeiateliers</li><li>Blog</li></ul></div>
    <div class="fcol testi"><h5>CLIENT'S TESTIMONIALS</h5><p>“Their clear advice helped us double our online leads in just six months.”</p><p>— Anne Verbeke, Bakkerij Lint</p></div>
    <div class="fcol touch"><h5>GET IN TOUCH</h5><p>Address: Stationsstraat 12, 9990 Veldhoek</p><p>Phone: 248-555-0147</p><p>Email: info@zaakkompas.be</p></div>
    <div class="fcol follow"><h5>FOLLOW US</h5><p>Connect with our social network</p><div class="follow-dots"><span></span><span></span><span></span></div></div>
  </div>
</footer>
<div class="copyright">Copyright © 2015. All rights reserved.</div>

</body>
</html>
```